pet minder needs a flyer design

I need a flyer design for my pet minding/ dog walking business.
My business is called 'Muddy paws happy tail crew', i would like the business
name included in on the flyer (i dont mind how big or small it is)
i was hoping for a design that was warm and friendly and obviously
incorporates animals :)
I have attached the information i would like included on the flyer below

Target Market(s)

all ages.

Industry/Entity Type

Pet Care

Font styles to use
Serif

Colors
ec1f27

Requirements
Must have
• information about the services i provide
• incorporates animals
Nice to have
• colour red

```html
<!DOCTYPE html>
<html lang="en">
<head>
<meta charset="utf-8">
<title>Muddy Paws Happy Tail Crew – Pet Sitter Flyer</title>
<link href="https://fonts.googleapis.com/css2?family=Arimo:wght@400;700&family=Cabin:wght@500;700&display=swap" rel="stylesheet">
<style>
  :root {
    --brand-red: #ec1f27;
    --deep-red: #c4161d;
    --ink: #1c1c1c;
    --paper: #ffffff;
    --panel: #f4f1f0;
    --wood-dark: #3b2316;
    --wood-mid: #5a3724;
    --grass-light: #b9c97a;
    --grass-dark: #5f7a2c;
    --silhouette: #d6d4d3;
  }
  html, body { margin: 0; padding: 0; overflow: hidden; }
  body { width: 872px; height: 1200px; background: var(--wood-dark); }

  .flyer {
    position: relative;
    width: 872px;
    height: 1200px;
    overflow: hidden;
    background: linear-gradient(90deg, var(--wood-dark), var(--wood-mid) 30%, var(--wood-dark) 55%, var(--wood-mid) 80%, var(--wood-dark));
  }
  .sheet {
    position: absolute;
    left: 22px; top: 22px;
    width: 828px; height: 1156px;
    background: var(--panel);
    overflow: hidden;
  }
  .hero-photo {
    position: absolute;
    left: 0; top: 0;
    width: 828px; height: 480px;
    background: linear-gradient(160deg, #e7ecc6 0%, var(--grass-light) 40%, var(--grass-dark) 100%);
  }
  .shapes { position: absolute; left: 0; top: 0; }

  .business-name {
    position: absolute;
    left: 30px; top: 26px;
    margin: 0;
    font-family: "Cabin", "Trebuchet MS", sans-serif;
    font-weight: 700;
    font-size: 20px;
    line-height: 24px;
    color: var(--paper);
  }

  .headline {
    position: absolute;
    left: 30px; top: 132px;
    margin: 0;
    font-family: "Arimo", Arial, sans-serif;
    font-weight: 700;
    font-size: 66px;
    line-height: 80px;
    color: var(--paper);
  }

  .intro {
    position: absolute;
    left: 48px; top: 530px;
    width: 770px;
    margin: 0;
    font-family: "Cabin", "Trebuchet MS", sans-serif;
    font-weight: 500;
    font-size: 38px;
    line-height: 58px;
    color: var(--brand-red);
  }

  .resting-dog {
    position: absolute;
    left: 580px; top: 765px;
    width: 230px; height: 130px;
    background: var(--silhouette);
    border-radius: 60px 70px 20px 20px;
  }

  .services-label {
    position: absolute;
    left: 0; top: 820px;
    width: 355px; height: 46px;
    background: var(--brand-red);
    clip-path: polygon(0 0, 92% 0, 100% 50%, 92% 100%, 0 100%);
    font-family: "Arimo", Arial, sans-serif;
    font-weight: 700;
    font-size: 30px;
    line-height: 46px;
    color: var(--paper);
    padding-left: 30px;
    box-sizing: border-box;
  }

  .service-list {
    position: absolute;
    left: 0; top: 0;
    margin: 0; padding: 0;
    list-style: none;
    font-family: "Arimo", Arial, sans-serif;
    font-size: 30px;
    color: var(--ink);
  }
  .service {
    position: absolute;
    white-space: nowrap;
    line-height: 36px;
    padding-left: 40px;
  }
  .service::before {
    content: "";
    position: absolute;
    left: 4px; top: 6px;
    width: 24px; height: 24px;
    border-radius: 50%;
    background: var(--brand-red);
  }

  .contact-bar {
    position: absolute;
    left: 0; bottom: 0;
    width: 828px; height: 74px;
    background: var(--brand-red);
    border-top: 4px solid var(--ink);
    box-sizing: border-box;
  }
  .contact-text {
    position: absolute;
    right: 18px; top: 12px;
    margin: 0;
    font-family: "Cabin", "Trebuchet MS", sans-serif;
    font-weight: 500;
    font-size: 36px;
    line-height: 46px;
    color: var(--paper);
  }
  .phone-badge { position: absolute; left: 14px; top: 1070px; }
  .dog-emblem {
    position: absolute;
    left: 572px; top: 436px;
    width: 60px; height: 44px;
    background: var(--deep-red);
    border-radius: 8px;
  }
</style>
</head>
<body>
<main class="flyer">
  <div class="sheet">
    <div class="hero-photo" role="img" aria-label="Photo of a woman walking a small fluffy dog on a lead across a sunny park lawn"></div>

    <svg class="shapes" width="828" height="560" viewBox="0 0 828 560" aria-hidden="true">
      <polygon points="0,0 130,0 602,440 828,378 828,412 602,476 0,520" fill="var(--brand-red)"/>
      <polygon points="0,520 602,476 828,412 828,560 0,560" fill="var(--panel)"/>
      <g transform="translate(602 458) rotate(45)">
        <rect x="-50" y="-50" width="100" height="100" fill="var(--ink)"/>
        <rect x="-44" y="-44" width="88" height="88" fill="var(--brand-red)"/>
      </g>
    </svg>
    <div class="dog-emblem" role="img" aria-label="Small black silhouette of a sitting dog"></div>

    <p class="business-name">Muddy paws happy tail crew</p>

    <h1 class="headline">Do<br>you<br>need a<br>petsitter?</h1>

    <p class="intro">I am a fully qualified<br>veterinary nurse who will<br>look after your animals like they<br>were my own own, when you go away!</p>

    <div class="resting-dog" role="img" aria-label="Faint grey silhouette of a dog lying down"></div>

    <div class="services-label">Services Provide</div>

    <ul class="service-list">
      <li class="service" style="left:8px;top:900px;">Pet Minding</li>
      <li class="service" style="left:278px;top:900px;">House Sitting</li>
      <li class="service" style="left:548px;top:900px;">Dog Walking</li>
      <li class="service" style="left:8px;top:958px;">Medication</li>
      <li class="service" style="left:278px;top:958px;">Collecting Mail/Watering Plants</li>
    </ul>

    <footer class="contact-bar">
      <p class="contact-text">enquire call me: Jodie 0400 123 456</p>
    </footer>

    <svg class="phone-badge" width="70" height="86" viewBox="0 0 70 86" aria-hidden="true">
      <rect x="12" y="16" width="46" height="46" transform="rotate(45 35 39)" fill="var(--ink)"/>
      <path d="M22 44 q0 -10 13 -10 q13 0 13 10 l-6 0 l-1 -4 q-6 -2 -12 0 l-1 4 z" fill="var(--paper)"/>
      <rect x="27" y="42" width="16" height="8" rx="2" fill="var(--paper)"/>
    </svg>
  </div>
</main>
</body>
</html>
```